The Quillmore Daily Ledger

I am making a journal for tracking pain symptoms for TMJ (Jaw) pain. I have the cover designed and I just need the journal page designed that will repeat throughout the journal. The journal is the image on the left of the bundle. The page I would like to be developed is the picture that I hand sketched out. It should be a 6 x 9 page, similar to the attached example. Greyscale, no color. Thank you!

Target Market(s)

20-55 year old women

Industry/Entity Type

Healthcare

Colors

Designer to choose only greyscale colors for use in the design.

Requirements
Must have
• A neat, well-designed page with the content I have sketched out by hand.
Nice to have
• Creative display of the content I provided and development of the pain scale and pain diagram faces in a professional looking way.

```html
<!DOCTYPE html>
<html lang="en">
<head>
<meta charset="utf-8">
<title>The Quillmore Daily Ledger — Daily Page</title>
<link href="https://fonts.googleapis.com/css2?family=Montserrat:wght@400;500;600&family=Source+Sans+3:wght@400;700&display=swap" rel="stylesheet">
<style>
  :root {
    --canvas: #ececec;
    --paper: #ffffff;
    --bar: #b8b8b8;
    --bar-text: #ffffff;
    --cell: #e3e3e3;
    --cell-line: #f7f7f7;
    --row-num: #cfcfcf;
    --box: #d9d9d9;
    --label: #ababab;
    --ink: #1a1a1a;
    --rule: #9a9a9a;
    --divider: #2a2a2a;
  }
  * { box-sizing: border-box; margin: 0; padding: 0; }
  html, body { width: 1200px; height: 900px; overflow: hidden; background: var(--canvas); }
  body { position: relative; font-family: "Montserrat", sans-serif; }

  .journal-page {
    position: absolute; left: 320px; top: 20px; width: 560px; height: 860px;
    background: var(--paper); box-shadow: 0 2px 10px rgba(0,0,0,.08);
  }
  .abs { position: absolute; }

  .bar {
    position: absolute; background: var(--bar); color: var(--bar-text);
    font-size: 9.5px; font-weight: 500; letter-spacing: .02em;
    display: flex; align-items: center;
  }
  .bar--center { justify-content: center; }
  .bar--left { padding-left: 7px; }

  .time-log { position: absolute; border-collapse: collapse; width: 229px; }
  .time-log th {
    background: var(--bar); color: var(--bar-text); font-weight: 500; font-size: 9.5px;
    height: 21px; border-right: 1px solid var(--cell-line);
  }
  .time-log td {
    background: var(--cell); height: 21px; border-right: 1px solid var(--bar);
    border-top: 1px solid var(--cell-line);
  }
  .time-log th:last-child, .time-log td:last-child { border-right: 0; }
  .time-log .row-num { width: 26px; background: var(--bar); color: var(--row-num); font-size: 9px; text-align: center; }
  .time-log tr:nth-child(odd) .row-num { color: var(--cell); }

  .check-row { position: absolute; display: flex; }
  .check {
    display: flex; align-items: center; gap: 5px;
    font-size: 10.5px; color: var(--label); white-space: nowrap;
  }
  .check::before {
    content: ""; width: 11px; height: 11px; background: var(--box); flex: none;
  }
  .scale .check { width: 53px; font-size: 10px; }

  .pain-map { position: absolute; left: 27px; top: 262px; width: 500px; height: 180px; display: flex; }
  .pain-type {
    flex: 1; display: flex; flex-direction: column; align-items: center;
    border-right: 1.2px solid var(--divider); padding-top: 4px;
  }
  .pain-type:last-child { border-right: 0; }
  .pain-figure {
    width: 66px; height: 96px; border-radius: 40% 40% 45% 45%;
    background: radial-gradient(circle at 50% 45%, #d0d0d0 0%, #8a8a8a 55%, #e8e8e8 100%);
  }
  .pain-name { font-family: "Source Sans 3", sans-serif; font-weight: 700; font-size: 11px; color: var(--ink); margin-top: 9px; }
  .pain-desc {
    font-family: "Source Sans 3", sans-serif; font-size: 9px; line-height: 11.5px;
    color: var(--ink); text-align: center; width: 62px;
  }

  .relief-other-line { position: absolute; left: 281px; top: 732px; width: 222px; border-top: 1px solid var(--rule); }
  .note-line { position: absolute; left: 27px; width: 503px; border-top: 1px solid var(--rule); }
</style>
</head>
<body>
<main class="journal-page">

  <div class="bar bar--left" style="left:29px;top:23px;width:170px;height:18px;">DATE</div>
  <div class="bar bar--left" style="left:299px;top:23px;width:228px;height:18px;">DAY OF THE WEEK</div>

  <table class="time-log" style="left:27px;top:63px;">
    <tr><th class="row-num"></th><th>BEGIN</th><th>END</th><th>DURATION</th></tr>
    <tr><td class="row-num">1</td><td></td><td></td><td></td></tr>
    <tr><td class="row-num">2</td><td></td><td></td><td></td></tr>
    <tr><td class="row-num">3</td><td></td><td></td><td></td></tr>
    <tr><td class="row-num">4</td><td></td><td></td><td></td></tr>
  </table>
  <table class="time-log" style="left:298px;top:63px;">
    <tr><th class="row-num"></th><th>BEGIN</th><th>END</th><th>DURATION</th></tr>
    <tr><td class="row-num">1</td><td></td><td></td><td></td></tr>
    <tr><td class="row-num">2</td><td></td><td></td><td></td></tr>
    <tr><td class="row-num">3</td><td></td><td></td><td></td></tr>
    <tr><td class="row-num">4</td><td></td><td></td><td></td></tr>
  </table>

  <div class="bar bar--center" style="left:27px;top:180px;width:500px;height:20px;">SEVERITY OF PAIN (CIRCLE RANGE)</div>
  <div class="check-row scale" style="left:27px;top:207px;">
    <span class="check">1</span><span class="check">2</span><span class="check">3</span><span class="check">4</span><span class="check">5</span><span class="check">6</span><span class="check">7</span><span class="check">8</span><span class="check">9</span><span class="check">10</span>
  </div>

  <div class="bar bar--center" style="left:27px;top:234px;width:500px;height:20px;">LOCATION</div>
  <section class="pain-map">
    <div class="pain-type"><div class="pain-figure" role="img" aria-label="Illustrated head in profile with shading at the temple and in front of the ear"></div><p class="pain-name">TMJ</p><p class="pain-desc">pain is at temples, in front of ears.</p></div>
    <div class="pain-type"><div class="pain-figure" role="img" aria-label="Illustrated head facing forward with shading over the brows and cheekbones"></div><p class="pain-name">Sinus</p><p class="pain-desc">pain is behind browbone and/or cheekbone.</p></div>
    <div class="pain-type"><div class="pain-figure" role="img" aria-label="Illustrated head with shading around one eye"></div><p class="pain-name">Cluster</p><p class="pain-desc">pain is in and around one eye.</p></div>
    <div class="pain-type"><div class="pain-figure" role="img" aria-label="Illustrated head with a shaded band across the forehead"></div><p class="pain-name">Tension</p><p class="pain-desc">pain is like a band squeezing the head.</p></div>
    <div class="pain-type"><div class="pain-figure" role="img" aria-label="Illustrated head with one half shaded"></div><p class="pain-name">Migraine</p><p class="pain-desc">pain, nausea and visual changes are typical of classic form.</p></div>
    <div class="pain-type"><div class="pain-figure" role="img" aria-label="Illustrated head in profile with shading at the back of the head"></div><p class="pain-name">Neck</p><p class="pain-desc">pain is at the top and/or back of head.</p></div>
  </section>

  <div class="bar bar--center" style="left:26px;top:455px;width:502px;height:21px;">TRIGGERS (CHECK ALL THAT APPLY)</div>
  <div class="abs" style="left:26px;top:484px;display:grid;grid-template-columns:162px 104px 148px 90px;row-gap:10px;">
    <span class="check">Sleep</span><span class="check">Insomnia</span><span class="check">Yawn</span><span class="check">Stress at Work</span>
    <span class="check">My First Thing in AM</span><span class="check">Eating</span><span class="check">PMS/ Menstration</span><span class="check">Weather</span>
    <span class="check">Clenching</span><span class="check">Work</span><span class="check">Stress at Home</span><span class="check">Other</span>
  </div>

  <div class="bar bar--center" style="left:26px;top:558px;width:120px;height:21px;">MY JAW WAS</div>
  <div class="check-row" style="left:151px;top:563px;gap:26px;"><span class="check">Clenched</span><span class="check">Relaxed</span></div>
  <div class="bar bar--center" style="left:26px;top:588px;width:120px;height:21px;">MY BREATH WAS</div>
  <div class="check-row" style="left:151px;top:593px;gap:35px;"><span class="check">Shallow</span><span class="check">Relaxed</span></div>
  <div class="bar bar--center" style="left:326px;top:558px;width:198px;height:21px;">MY NECK/ SHOULDERS WERE</div>
  <div class="check-row" style="left:326px;top:587px;gap:36px;"><span class="check">Tense</span><span class="check">Relaxed</span></div>

  <div class="bar bar--center" style="left:25px;top:628px;width:504px;height:21px;">RELIEF MEASURES (CHECK ALL THAT APPLY)</div>
  <div class="abs" style="left:25px;top:657px;display:grid;grid-template-columns:224px 168px 112px;row-gap:10px;">
    <span class="check">Deep Breathing</span><span class="check">Heat/ Cold</span><span class="check">Gentle Stretching</span>
    <span class="check">Teeth apart/ Relax jaw</span><span class="check">Medication</span><span class="check">Posture Correction</span>
    <span class="check">Self Massage</span><span class="check">Rest</span><span class="check">Mindful Reset</span>
    <span class="check">Stabilization Exercise</span><span class="check">Others</span><span></span>
  </div>
  <div class="relief-other-line" style="left:309px;width:221px;"></div>

  <div class="bar bar--center" style="left:27px;top:754px;width:503px;height:21px;">NOTES AND PLANS TO AVOID TRIGGERS</div>
  <div class="note-line" style="top:797px;"></div>
  <div class="note-line" style="top:816px;"></div>
  <div class="note-line" style="top:835px;"></div>

</main>
</body>
</html>
```